Company brochure for our unique consulting business

We are a small consulting business offering a unique set of services to our clients.. In simple terms we are a business improvement consultancy helping our clients get the best out of their businesses. We work with clients across multiple sectors and deliver a variety of services. We want to put together a brochure to cover these main themes:1. Who we are2. What we do3. The type of people we employ4. The sectors we work inWhile the brochure needs to have a certain corporate feel to it, we don't want it to be "boring" or "stiff". We would like it to have a slightly "friendly" or "informal" feel to it, to reflect the type of organisation we are.We have a company website http://tollandvergeadvisory.com , however we do not want to directly replicate the content or feel as we recognise it needs updating.We would like the brochure to be A4 portrait format. We anticipate requiring 12 sides (including covers) but we are happy to be guided on this based on the content we have provided.The attached ppt file gives the detail of the content to be included and also shows the proposed pagination. For the front cover we would like to try 2 versions, one with the TVA logo and one with the Tolland Verge Advisory logo (a file of both is attached)One of the most important pages will be the "Our Services" page. We would like this to cover the centre fold. In the ppt file we have shown an example layout, but this is where we need most help - we are clearly not graphic designers! This page will be the most used page in sales meetings etc.Also attached is the following:1. file for our TollandVerge Advisory company logo.2. File for our TVA company logo3. Files for Derek's signatures (for under photos) - Owen's to follow4. Photo of Derek & Owen (person in purple shirt to be cropped out)Thank you and really excited to see what everyone comes back with.Derek & Owen

Target Market(s)

Very broad - Manufacturing, Healthcare, Hospitality

Industry/Entity Type

Management Consulting

Font styles to use
Other font styles liked:
• We use Swiss721, but happy to be guided by designer

Colors
3276b5
85abd2
0355a3
333333
5c5c5c
9d9d9d
d9d9d9

Requirements
Must have
• Corporate feel
Nice to have
• Slightly friendly feel
• Our standard "blue" is (CORRECTION) - R55 G96 B146 #376092 and our standard grey is R197 G178, B179 - #B3B2B2, which we would like to keep, but other colours we are happy to be guided on. Brand guidelines attached.

```html
<!DOCTYPE html>
<html lang="en">
<head>
<meta charset="utf-8">
<title>Tolland Verge Advisory – Values and About Us spread</title>
<link rel="stylesheet" href="https://fonts.googleapis.com/css2?family=Lato:ital,wght@0,400;0,700;0,900;1,900&display=swap">
<style>
  :root{
    --brand-blue:#376092;
    --band-blue:#4a6b9f;
    --deep-blue:#2f4f80;
    --ink:#333333;
    --ink-soft:#5c5c5c;
    --paper:#f4f5f8;
    --backdrop:#333336;
  }
  *{box-sizing:border-box;margin:0;padding:0}
  html,body{width:1200px;height:789px;overflow:hidden;background:var(--backdrop)}
  body{font-family:"Lato",sans-serif;color:var(--ink)}
  .spread{position:absolute;left:105px;top:44px;width:990px;height:700px;display:flex}
  .page{position:relative;width:495px;height:700px;background:var(--paper);overflow:hidden}
  .page--left{box-shadow:inset -14px 0 18px -14px rgba(0,0,0,.25)}
  .page--right{box-shadow:inset 14px 0 18px -14px rgba(0,0,0,.25)}
  .heading{position:absolute;font-weight:900;font-style:italic;font-size:27px;letter-spacing:-.3px;color:var(--ink)}
  .heading .accent{color:var(--brand-blue)}
  .heading::after{content:"";position:absolute;left:0;bottom:-5px;width:78px;height:2px;background:var(--ink)}
  .values-heading{left:38px;top:48px}
  .about-heading{left:30px;top:70px;font-style:normal;font-weight:700}
  .about-heading::after{width:92px}
  .values-photo{position:absolute;left:32px;top:100px;width:238px;height:338px;
    background:linear-gradient(135deg,#6f7278 0%,#b9bcc2 40%,#4f7fc2 75%,#2d5ea8 100%)}
  .values-list{position:absolute;left:288px;top:110px;width:180px;font-size:11.5px;line-height:1.28;color:var(--ink)}
  .values-list p{margin-bottom:9px}
  .page-band{position:absolute;left:0;bottom:0;width:495px;height:170px}
  .page-num{position:absolute;width:26px;height:26px;border-radius:50%;background:var(--deep-blue);color:#fff;
    font-size:10px;font-weight:700;display:flex;align-items:center;justify-content:center}
  .page--left .page-num{right:36px;bottom:44px}
  .page--right .page-num{left:20px;bottom:40px}
  .team-photo{position:absolute;left:0;top:118px;width:495px;height:340px;
    background:linear-gradient(160deg,#eceae6 0%,#dcd7d0 40%,#9fb6d8 70%,#c9a27e 100%);
    clip-path:polygon(0 0,100% 0,100% 87%,0 62%)}
  .photo-stripe{position:absolute;left:0;top:320px;width:495px;height:110px}
  .name-tab{position:absolute;width:150px;height:58px;padding-top:9px;
    background:var(--band-blue);color:#fff;text-align:center;font-size:16px;line-height:1.15;
    clip-path:polygon(0 0,100% 0,88% 100%,12% 100%);
    transform:rotate(10deg);transform-origin:0 0}
  .name-tab--owen{left:62px;top:336px}
  .name-tab--derek{left:300px;top:378px}
  .signature{position:absolute;height:14px;background:linear-gradient(90deg,#9aa0a8,#c9ccd1);opacity:.7;border-radius:2px;
    transform:rotate(10deg);transform-origin:0 0}
  .signature--owen{left:78px;top:418px;width:90px}
  .signature--derek{left:318px;top:462px;width:100px}
  .bio{position:absolute;font-size:11.5px;line-height:1.3;color:var(--ink-soft);text-align:center;
    transform:rotate(10deg);transform-origin:0 0}
  .bio--owen{left:62px;top:440px;width:180px}
  .bio--derek{left:300px;top:485px;width:190px}
</style>
</head>
<body>
<main class="spread">
  <section class="page page--left">
    <h2 class="heading values-heading"><span class="accent">OUR</span> VALUES</h2>
    <div class="values-photo" role="img" aria-label="Photo of a hand touching a glowing blue bar chart on a digital screen"></div>
    <div class="values-list">
      <p>Be TRUSTED by our team and clients, so that our opinions are sought and our recommendations valued.</p>
      <p>Have a tight knit relationship with our clients, so we are seen as a PARTNER and not just supplier.</p>
      <p>Be focused on return-on-investment, but predominantly, always deliver GREAT VALUE.</p>
      <p>DEVELOP &amp; INVEST IN our own people to continually stay one step ahead.</p>
      <p>Work relentlessly to deliver results for our clients, but ensure we collectively ENJOY THE JOURNEY.</p>
      <p>Take SOCIAL RESPONSIBILITY seriously by supporting other worthwhile organisations.</p>
    </div>
    <svg class="page-band" viewBox="0 0 495 170" aria-hidden="true">
      <path d="M0 38 C160 40 330 90 495 150 L495 160 C330 102 160 52 0 50 Z" fill="var(--band-blue)"/>
    </svg>
    <div class="page-num">02</div>
  </section>

  <section class="page page--right">
    <h2 class="heading about-heading"><span class="accent">About</span> Us</h2>
    <div class="team-photo" role="img" aria-label="Photo of the two partners smiling at a meeting table"></div>
    <svg class="photo-stripe" viewBox="0 0 495 110" aria-hidden="true">
      <path d="M0 8 L495 95 L495 105 L0 18 Z" fill="var(--band-blue)"/>
    </svg>
    <div class="name-tab name-tab--owen">Owen Tolland<br>Partner</div>
    <div class="name-tab name-tab--derek">Derek Verge<br>Partner</div>
    <div class="signature signature--owen" role="img" aria-label="Owen's signature"></div>
    <div class="signature signature--derek" role="img" aria-label="Derek's signature"></div>
    <p class="bio bio--owen">At TVA we constantly strive to deliver the best possible value for our clients. Importantly we recognize, it's our clients that define value, not us.</p>
    <p class="bio bio--derek">We bring together our expertise from Kestrel Motors and our experience of working with multiple organisations to help our clients deliver results against their own individual goals.</p>
    <svg class="page-band" viewBox="0 0 495 170" aria-hidden="true">
      <path d="M0 118 C140 110 330 130 495 158 L495 170 C330 142 140 124 0 130 Z" fill="var(--band-blue)"/>
    </svg>
    <div class="page-num">03</div>
  </section>
</main>
</body>
</html>
```